Black Granite Web Design Project

We are looking for a design for a new company that will be selling Black Granite slabs and tiles. We will be selling to both end-consumers and granite installers. We have already settled on a logo and hopefully this will give an idea of what we like in our designs. We are not going to be selling online but want people to call us so the site is basically an enhanced business card. We will be focusing a lot on SEO so the design will have to keep that in mind.

We would like to keep the design in 1024x768 to make it easily view-able on all devices.

Regarding navigation there should only be a few sub-pages, like "Granite Slabs", "Granite Tiles", "Delivery", "Contact"

Aside from that we are open to designs. One idea we did have was to personalize the site and have a person there somehow to represent the company, making the user feel there are real people behind this site. This is just an idea and not a must.

The name of the company and site is "Copper Ridge Pietra"

Thanks
Updates

Hello All,

Thanks for the great designs. There are some good looking designs that show beautiful kitchens but this site is made for the granite installers and not the retail consumers. So in order not to to confuse the buyers I would like to keep this as much about the raw products as possible. The raw products being the granite slabs, thereby making it obvious we don't sell granite counter tops. 

This design will really be the identity of this company so it is important we get the right message across on this index page and that this page is as complete as possible.

Again, thanks for all the work being put into this.

Target Market(s)

The target audience is granite installers or companies that would with granite slabs.

Industry/Entity Type

Business

```html
<!DOCTYPE html>
<html lang="en">
<head>
<meta charset="utf-8">
<title>Copper Ridge Pietra</title>
<link href="https://fonts.googleapis.com/css2?family=Archivo+Black&family=Arimo:wght@400;700&family=Roboto:wght@500&display=swap" rel="stylesheet">
<style>
:root{
  --black:#000;
  --panel:#161616;
  --btn:#2b2b2b;
  --decor:#1b1b1b;
  --white:#fff;
  --ink:#1a1a1a;
  --heading:#3a1610;
  --link:#1f3f8f;
  --navy:#1f3550;
}
*{margin:0;padding:0;box-sizing:border-box}
html,body{width:1200px;height:1078px;overflow:hidden;background:var(--white)}
body{position:relative;font-family:"Arimo",Arial,sans-serif;color:var(--ink)}
.abs{position:absolute}

.masthead{left:0;top:0;width:1200px;height:554px;background:var(--black)}
.masthead-texture{left:0;top:0;width:1200px;height:160px;
  background:radial-gradient(ellipse at 20% 30%,#3b4030 0,transparent 55%),
             radial-gradient(ellipse at 75% 25%,#34382a 0,transparent 50%),
             linear-gradient(180deg,#2a2c22 0,#15160f 70%,#000 100%)}
.brand{left:0;top:40px;width:1200px;text-align:center}
.brand-mark{display:block;width:40px;height:40px;background:var(--white);margin:0 auto 14px}
.brand-name{font-family:"Archivo Black",sans-serif;color:var(--white);font-size:30px;letter-spacing:.5px;line-height:1}

.decor{height:49px;top:167px;
  background:linear-gradient(var(--black),var(--black)) 0 23px/100% 3px no-repeat,
             repeating-linear-gradient(90deg,var(--decor) 0 26px,var(--black) 26px 29px)}
.swatch{width:23px;height:49px;top:167px;display:flex;flex-direction:column;gap:3px}
.swatch i{flex:1}
.nav-item{top:167px;height:49px;width:170px;background:var(--btn);color:var(--white);
  font-family:"Archivo Black",sans-serif;font-size:16px;letter-spacing:.3px;
  display:flex;align-items:center;justify-content:center;text-decoration:none}
.nav-item.active{background:repeating-linear-gradient(135deg,#2e2e2e 0 4px,#3a3a3a 4px 7px)}

.gallery{left:180px;top:231px;width:846px;height:306px;background:var(--panel)}
.gallery-divider{left:813px;top:231px;width:3px;height:306px;background:#000}
.slab{width:93px;height:93px}
.arrow{top:359px;width:27px;height:50px;background:#2a2a2a;display:flex;align-items:center;justify-content:center}

.rule{left:0;width:1200px;height:7px;background:repeating-linear-gradient(90deg,#000 0 2px,#fff 2px 4px)}

.intro{left:191px;top:572px;width:805px}
.intro-icon{position:absolute;left:0;top:0}
.intro h1{font-family:"Roboto",sans-serif;font-weight:500;font-size:16px;color:var(--heading);margin-left:32px;line-height:20px;padding-top:6px}
.intro p{font-size:12px;line-height:16.2px;margin:6px 0 0 19px;text-indent:13px}
.intro a{color:var(--link)}

.founder{width:170px;text-align:center;top:800px}
.portrait{width:138px;height:138px;border-radius:50%;margin:0 auto 17px}
.founder p{font-size:12.5px;line-height:16px}

.footer{left:0;top:1006px;width:1200px;height:72px;background:var(--black)}
.footer-brand{left:199px;top:1024px;display:flex;align-items:center;gap:12px}
.footer-brand i{width:30px;height:30px;background:var(--white)}
.footer-brand span{font-family:"Archivo Black",sans-serif;color:var(--white);font-size:25px}
.callout{left:780px;top:1023px;color:var(--white)}
.callout small{display:block;font-family:"Arimo",sans-serif;font-weight:700;font-size:12px}
.callout strong{display:block;font-family:"Archivo Black",sans-serif;font-size:27px;line-height:30px;font-weight:400}
</style>
</head>
<body>

<header class="abs masthead">
  <div class="abs masthead-texture" role="img" aria-label="Dark granite texture banner"></div>
  <div class="abs brand"><span class="brand-mark"></span><span class="brand-name">COPPER RIDGE PIETRA</span></div>
</header>

<nav>
  <div class="abs decor" style="left:0;width:206px"></div>
  <div class="abs swatch" style="left:184px"><i style="background:#3a4440"></i><i style="background:#2a3834"></i></div>
  <a class="abs nav-item active" style="left:210px">GRANITE SLABS</a>
  <div class="abs swatch" style="left:396px"><i style="background:#1d2d40"></i><i style="background:#203c5a"></i></div>
  <a class="abs nav-item" style="left:423px">GRANITE TILES</a>
  <div class="abs swatch" style="left:609px"><i style="background:#4a4232"></i><i style="background:#2e2a18"></i></div>
  <a class="abs nav-item" style="left:636px">DELIVERY</a>
  <div class="abs swatch" style="left:823px"><i style="background:#4a2418"></i><i style="background:#2e1c16"></i></div>
  <a class="abs nav-item" style="left:850px">CONTACT</a>
  <div class="abs decor" style="left:1027px;width:173px"></div>
</nav>

<section class="abs gallery" aria-label="Granite samples"></section>
<div class="abs gallery-divider"></div>

<!-- row 1 -->
<div class="abs slab" style="left:183px;top:232px;background:linear-gradient(135deg,#c8c8c8,#7a7a7a)" role="img" aria-label="Grey granite sample"></div>
<div class="abs slab" style="left:290px;top:232px;background:linear-gradient(135deg,#bdbdbd,#6e6e6e)" role="img" aria-label="Grey granite sample"></div>
<div class="abs slab" style="left:396px;top:232px;background:linear-gradient(135deg,#8a7d5c,#4a4330)" role="img" aria-label="Olive granite sample"></div>
<div class="abs slab" style="left:501px;top:232px;background:linear-gradient(135deg,#d49a78,#9a5a3e)" role="img" aria-label="Rose granite sample"></div>
<div class="abs slab" style="left:607px;top:232px;background:linear-gradient(135deg,#b8654a,#5a2e22)" role="img" aria-label="Red granite sample"></div>
<div class="abs slab" style="left:712px;top:232px;background:linear-gradient(135deg,#c84a24,#6a1e10)" role="img" aria-label="Bright red granite sample"></div>
<div class="abs slab" style="left:819px;top:232px;background:linear-gradient(135deg,#c8c8c8,#7a7a7a)" role="img" aria-label="Grey granite sample"></div>
<div class="abs slab" style="left:925px;top:232px;background:linear-gradient(135deg,#bdbdbd,#6e6e6e)" role="img" aria-label="Grey granite sample"></div>
<!-- row 2 -->
<div class="abs slab" style="left:183px;top:338px;background:linear-gradient(135deg,#8a6a48,#4a5a34)" role="img" aria-label="Brown green granite sample"></div>
<div class="abs slab" style="left:290px;top:338px;background:linear-gradient(135deg,#9a9490,#5e5650)" role="img" aria-label="Grey granite sample"></div>
<div class="abs slab" style="left:396px;top:338px;background:linear-gradient(135deg,#3a4a40,#0e1612)" role="img" aria-label="Dark granite sample"></div>
<div class="abs slab" style="left:501px;top:338px;background:linear-gradient(135deg,#b88a72,#6a3a2a)" role="img" aria-label="Pink granite sample"></div>
<div class="abs slab" style="left:607px;top:338px;background:linear-gradient(135deg,#c0bcaa,#5e5c4e)" role="img" aria-label="Speckled granite sample"></div>
<div class="abs slab" style="left:712px;top:338px;background:linear-gradient(135deg,#3e5a34,#1a2a16)" role="img" aria-label="Green granite sample"></div>
<div class="abs slab" style="left:819px;top:338px;background:linear-gradient(135deg,#8a6a48,#4a5a34)" role="img" aria-label="Brown green granite sample"></div>
<div class="abs slab" style="left:925px;top:338px;background:linear-gradient(135deg,#9a9490,#5e5650)" role="img" aria-label="Grey granite sample"></div>
<!-- row 3 -->
<div class="abs slab" style="left:183px;top:443px;background:linear-gradient(135deg,#d09a7c,#8a5a42)" role="img" aria-label="Rose granite sample"></div>
<div class="abs slab" style="left:290px;top:443px;background:linear-gradient(135deg,#a89a5a,#3a3a1e)" role="img" aria-label="Gold granite sample"></div>
<div class="abs slab" style="left:396px;top:443px;background:linear-gradient(135deg,#c8623a,#7a2e18)" role="img" aria-label="Orange granite sample"></div>
<div class="abs slab" style="left:501px;top:443px;background:linear-gradient(135deg,#d4764a,#8a3a20)" role="img" aria-label="Orange granite sample"></div>
<div class="abs slab" style="left:607px;top:443px;background:linear-gradient(135deg,#a86a4a,#3a2418)" role="img" aria-label="Brown granite sample"></div>
<div class="abs slab" style="left:712px;top:443px;background:linear-gradient(135deg,#a8aaa6,#6e726e)" role="img" aria-label="Light grey granite sample"></div>
<div class="abs slab" style="left:819px;top:443px;background:linear-gradient(135deg,#d09a7c,#8a5a42)" role="img" aria-label="Rose granite sample"></div>
<div class="abs slab" style="left:925px;top:443px;background:linear-gradient(135deg,#a89a5a,#3a3a1e)" role="img" aria-label="Gold granite sample"></div>

<div class="abs arrow" style="left:180px"><svg width="10" height="14" viewBox="0 0 10 14"><path d="M2 1l6 6-6 6" fill="none" stroke="#777" stroke-width="2.5"/></svg></div>
<div class="abs arrow" style="left:998px"><svg width="10" height="14" viewBox="0 0 10 14"><path d="M8 1L2 7l6 6" fill="none" stroke="#777" stroke-width="2.5"/></svg></div>

<div class="abs rule" style="top:554px"></div>

<main class="abs intro">
  <svg class="intro-icon" width="20" height="20" viewBox="0 0 20 20"><rect x="0" y="0" width="9" height="9" fill="#1f3550"/><rect x="11" y="0" width="9" height="9" fill="#1f3550"/><rect x="0" y="11" width="9" height="9" fill="#1f3550"/></svg>
  <h1>Just H1 heading text</h1>
  <p>Contrary to popular belief, Lorem Ipsum is not simply random text. It has roots in a piece of classical Latin literature from 45 BC, making it over 2000 years old. Elias Brandt, a Latin professor at Harrow Point College in Virginia, looked up one of the more obscure Latin words, consectetur, from a Lorem Ipsum passage, and going through the cites of the word in classical literature, discovered the undoubtable source. Lorem Ipsum comes from sections 1.10.32 and 1.10.33 of "de<br>&nbsp;&nbsp;&nbsp;&nbsp;Finibus <a href="#">Bonorum et Malorum</a>" (The Extremes of Good and Evil) by Lucan Orbis, written in 45 BC. This book is a treatise on the theory of ethics, very popular during the Renaissance. Contrary to popular belief, Lorem Ipsum is not simply random text. It has roots in a piece of classical Latin literature from 45 BC, making it over 2000 years old. Elias Brandt, a Latin professor at Harrow Point College in Virginia, looked up one of the more obscure Latin words, consectetur, from a Lorem Ipsum passage, and going through the cites of the word in classical literature, discovered the undoubtable source. Lorem Ipsum comes from sections 1.10.32 and 1.10.33 of "de Finibus Bonorum et Malorum" (The Extremes of Good and Evil) by Lucan Orbis, written in 45 BC. This book is a treatise on the theory of ethics, very popular during the Renaissance.</p>
</main>

<div class="abs founder" style="left:194px"><div class="portrait" role="img" aria-label="Portrait of co-founder" style="background:radial-gradient(circle at 50% 45%,#b08a6a,#6a5a3e 60%,#1e2a40)"></div><p>Dario Vale<br>Co Founder</p></div>
<div class="abs founder" style="left:409px"><div class="portrait" role="img" aria-label="Portrait of co-founder" style="background:radial-gradient(circle at 50% 45%,#8a8a8a,#2a2a2a 60%,#0e0e0e)"></div><p>Dario Vale<br>Co Founder</p></div>
<div class="abs founder" style="left:630px"><div class="portrait" role="img" aria-label="Portrait of co-founder" style="background:radial-gradient(circle at 50% 45%,#b08a6a,#6a5a3e 60%,#1e2a40)"></div><p>Dario Vale<br>Co Founder</p></div>
<div class="abs founder" style="left:837px"><div class="portrait" role="img" aria-label="Portrait of co-founder" style="background:radial-gradient(circle at 50% 45%,#8a8a8a,#2a2a2a 60%,#0e0e0e)"></div><p>Dario Vale<br>Co Founder</p></div>

<div class="abs rule" style="top:999px"></div>

<footer class="abs footer"></footer>
<div class="abs footer-brand"><i></i><span>COPPER RIDGE PIETRA</span></div>
<div class="abs callout"><small>Call us:</small><strong>1-877-555-0142</strong></div>

</body>
</html>
```